VelgoNexus PowerPoint Design

We need a very cool power-point template done for VelgoNexus. We need it to drive the message of technology, speed and innovation. This is for a racing proposal to for our indy car team. I will attach our logo.

Target Market(s)

This presentation is for our INDY RACE CAR TEAM OVERVIEW... The Theme is: Speed, Technology and Innovation

Industry/Entity Type

Racing

Colors

Designer to choose colors to be used in the design.

Requirements
Must have
• Intro Slide with Logo - Must look very cool
Template Slide for Content
Ending Slide with something like "Thanks VelgoNexus!"
Nice to have
• Please see the example ppt deck from Morbeck a previous company to see the slide template... Also see a old template for VelgoNexus

```html
<!DOCTYPE html>
<html lang="en">
<head>
<meta charset="utf-8">
<title>VelgoNexus Indy Racing Presentation Template</title>
<link rel="stylesheet" href="https://fonts.googleapis.com/css2?family=Ubuntu:wght@400;500;700&family=Mr+Dafoe&display=swap">
<style>
  :root {
    --stage-dark: #2a2a2b;
    --stage-light: #5a5a5c;
    --blue-light: #1769a3;
    --blue-deep: #0e5686;
    --brand-blue: #2683c2;
    --accent-orange: #f6a823;
    --swoosh-grey: #d9d6d0;
    --paper: #ffffff;
    --paper-shade: #ecedee;
    --body-ink: #111111;
  }
  * { box-sizing: border-box; margin: 0; padding: 0; }
  html, body { width: 1200px; height: 999px; overflow: hidden; }
  body {
    background: radial-gradient(ellipse at 50% 45%, var(--stage-light) 0%, #444446 45%, var(--stage-dark) 100%);
    font-family: "Ubuntu", sans-serif;
    position: relative;
  }
  .slide {
    position: absolute;
    width: 539px;
    height: 405px;
    overflow: hidden;
    box-shadow: 0 0 0 1px rgba(255,255,255,0.15);
  }
  .slide--intro     { left: 34px;  top: 79px; }
  .slide--content-a { left: 628px; top: 81px; }
  .slide--content-b { left: 34px;  top: 514px; }
  .slide--closing   { left: 627px; top: 513px; }
  .slide__art { position: absolute; inset: 0; width: 100%; height: 100%; }

  .brand { position: absolute; left: 0; right: 0; text-align: center; }
  .brand__name {
    display: inline-block;
    font-size: 45px; font-weight: 500; letter-spacing: -0.5px;
    color: var(--brand-blue); line-height: 1;
    padding: 0 4px 5px; border-bottom: 1px solid var(--brand-blue);
  }
  .brand__tagline { font-size: 14px; font-weight: 500; color: var(--brand-blue); margin-top: 4px; }
  .site-url {
    position: absolute; left: 0; right: 0; text-align: center;
    font-size: 22px; font-weight: 700; color: var(--brand-blue);
  }
  .slide__title {
    position: absolute; left: 30px; top: 28px;
    font-size: 23px; font-weight: 500; color: var(--paper); letter-spacing: 0.3px;
  }
  .slide__body {
    position: absolute; left: 30px; top: 150px; width: 476px;
    font-family: Arial, Helvetica, sans-serif;
    font-size: 11.3px; line-height: 14.4px; color: var(--body-ink);
    text-align: justify;
  }
  .slide__body p + p { margin-top: 14px; }
  .url-pill {
    position: absolute; right: 22px; bottom: 5px;
    background: var(--blue-deep); color: var(--paper);
    border: 2px solid var(--paper); border-radius: 12px;
    font-family: Arial, Helvetica, sans-serif; font-weight: 700; font-size: 10px;
    padding: 4px 9px;
  }
  .closing-word {
    position: absolute; left: 0; right: 0; top: 10px; text-align: center;
    font-family: "Mr Dafoe", cursive; font-size: 100px; color: var(--paper);
  }
</style>
</head>
<body>

<section class="slide slide--intro">
  <svg class="slide__art" viewBox="0 0 539 405" preserveAspectRatio="none" aria-hidden="true">
    <defs>
      <radialGradient id="paperGlow" cx="50%" cy="60%" r="70%">
        <stop offset="0" stop-color="var(--paper)"/><stop offset="1" stop-color="var(--paper-shade)"/>
      </radialGradient>
    </defs>
    <rect width="539" height="405" fill="var(--blue-light)"/>
    <path d="M0 125 C140 95 300 45 539 70 L539 260 L0 260 Z" fill="var(--blue-deep)"/>
    <path d="M0 186 C120 150 230 146 330 165 C430 184 490 170 539 140 L539 405 L0 405 Z" fill="var(--swoosh-grey)"/>
    <path d="M0 194 C120 158 230 154 330 173 C430 192 490 178 539 148 L539 405 L0 405 Z" fill="#ffffff"/>
    <path d="M0 202 C120 166 230 162 330 181 C430 200 490 186 539 156 L539 405 L0 405 Z" fill="url(#paperGlow)"/>
    <rect y="392" width="539" height="13" fill="var(--blue-light)"/>
  </svg>
  <div class="brand" style="top:248px;">
    <div class="brand__name">VelgoNexus</div>
    <div class="brand__tagline">Speed, Technology and Innovation on Every Lap</div>
  </div>
  <div class="site-url" style="top:355px;">www.velgonexus.com</div>
</section>

<section class="slide slide--content-a">
  <svg class="slide__art" viewBox="0 0 539 405" preserveAspectRatio="none">
    <defs>
      <radialGradient id="paperGlowA" cx="50%" cy="55%" r="70%">
        <stop offset="0" stop-color="var(--paper)"/><stop offset="1" stop-color="var(--paper-shade)"/>
      </radialGradient>
    </defs>
    <rect width="539" height="405" fill="var(--blue-light)"/>
    <path d="M0 72 C100 100 200 115 300 90 C400 60 450 40 539 125 L539 405 L0 405 Z" fill="var(--swoosh-grey)"/>
    <path d="M0 64 C100 92 200 107 300 82 C400 52 450 32 539 117 L539 405 L0 405 Z" fill="var(--accent-orange)"/>
    <path d="M0 68 C100 96 200 111 300 86 C400 56 450 36 539 121 L539 405 L0 405 Z" fill="#ffffff"/>
    <path d="M0 80 C100 108 200 123 300 98 C400 68 450 48 539 133 L539 405 L0 405 Z" fill="url(#paperGlowA)"/>
    <ellipse cx="450" cy="115" rx="70" ry="30" fill="#e7e9ee" role="img" aria-label="Faint racing flag motif"/>
    <rect y="392" width="539" height="13" fill="var(--blue-light)"/>
  </svg>
  <h2 class="slide__title">TEAM OVERVIEW</h2>
  <div class="slide__body">
    <p>VelgoNexus Racing brings together engineers, drivers and strategists who share one goal: to be the fastest team on the grid. Our program blends proven race craft with modern data tools, so every decision in the garage and on the pit wall is backed by live telemetry. From the first test day to the final checkered flag, the team works as one unit, refining setups, tuning aerodynamics and sharpening pit stops. This season we aim to turn that focus into podium results and a lasting partnership with our sponsors.</p>
    <p>Our crew pairs seasoned race engineers with young talent from leading technical schools. Together they run simulation work between events, study tire wear lap by lap and build race plans for every circuit on the calendar. Partners gain a visible place on the car, the transporter and the team apparel, plus access to hospitality at each race weekend. We invite you to join the VelgoNexus program and share in the speed, the technology and the innovation that drive us forward.</p>
  </div>
  <div class="url-pill">www.velgonexus.com</div>
</section>

<section class="slide slide--content-b">
  <svg class="slide__art" viewBox="0 0 539 405" preserveAspectRatio="none">
    <defs>
      <radialGradient id="paperGlowB" cx="50%" cy="55%" r="70%">
        <stop offset="0" stop-color="var(--paper)"/><stop offset="1" stop-color="var(--paper-shade)"/>
      </radialGradient>
    </defs>
    <rect width="539" height="405" fill="var(--blue-light)"/>
    <path d="M0 72 C100 100 200 115 300 90 C400 60 450 40 539 125 L539 405 L0 405 Z" fill="var(--swoosh-grey)"/>
    <path d="M0 64 C100 92 200 107 300 82 C400 52 450 32 539 117 L539 405 L0 405 Z" fill="var(--accent-orange)"/>
    <path d="M0 68 C100 96 200 111 300 86 C400 56 450 36 539 121 L539 405 L0 405 Z" fill="#ffffff"/>
    <path d="M0 80 C100 108 200 123 300 98 C400 68 450 48 539 133 L539 405 L0 405 Z" fill="url(#paperGlowB)"/>
    <ellipse cx="450" cy="115" rx="70" ry="30" fill="#e7e9ee" role="img" aria-label="Faint racing flag motif"/>
    <rect y="390" width="539" height="15" fill="var(--blue-light)"/>
  </svg>
  <h2 class="slide__title">TECHNOLOGY</h2>
  <div class="slide__body">
    <p>Every VelgoNexus car carries hundreds of sensors that stream data to the pit wall in real time. Engineers read engine load, brake temperature and tire pressure as the car races, and adjust strategy within seconds. Back at the shop, our simulation suite replays each session so drivers can rehearse braking points and racing lines before they reach the track. This constant loop of data, testing and feedback keeps the car sharp, the crew ready and the team one step ahead of the field on every type of circuit.</p>
    <p>Innovation is not limited to the car. We use lightweight composites in our pit equipment, digital checklists for every stop and smart scheduling to keep crews rested and alert. Our partners share in this work through joint research, branded content and technical showcases at race events. Together we can show fans how modern engineering turns raw speed into consistent results, and how a focused team can push the limits of what an Indy car can do on race day.</p>
  </div>
  <div class="url-pill" style="bottom:4px;">www.velgonexus.com</div>
</section>

<section class="slide slide--closing">
  <svg class="slide__art" viewBox="0 0 539 405" preserveAspectRatio="none" aria-hidden="true">
    <defs>
      <radialGradient id="paperGlowC" cx="50%" cy="65%" r="70%">
        <stop offset="0" stop-color="var(--paper)"/><stop offset="1" stop-color="var(--paper-shade)"/>
      </radialGradient>
    </defs>
    <rect width="539" height="405" fill="var(--blue-light)"/>
    <path d="M0 150 C140 120 300 60 539 60 L539 300 L0 300 Z" fill="var(--blue-deep)"/>
    <path d="M0 190 C120 150 230 146 330 160 C430 176 490 165 539 140 L539 405 L0 405 Z" fill="var(--swoosh-grey)"/>
    <path d="M0 198 C120 158 230 154 330 168 C430 184 490 173 539 148 L539 405 L0 405 Z" fill="#ffffff"/>
    <path d="M0 206 C120 166 230 162 330 176 C430 192 490 181 539 156 L539 405 L0 405 Z" fill="url(#paperGlowC)"/>
    <rect y="392" width="539" height="13" fill="var(--blue-light)"/>
  </svg>
  <div class="closing-word">Thanks</div>
  <div class="brand" style="top:248px;">
    <div class="brand__name">VelgoNexus</div>
    <div class="brand__tagline">Speed, Technology and Innovation on Every Lap</div>
  </div>
  <div class="site-url" style="top:355px;">www.velgonexus.com</div>
</section>

</body>
</html>
```